Brindle Financial Advice - Employer Benefit Brochure

We need to design a professional looking brochure that we can present to our existing client base, and assist in attracting new clients.
The current information is just provided in a word document, but we need to improve significantly.
The audience would be business leaders, HR decision makers and member policy committee members

Industry/Entity Type

Business

Font styles to use
Sans Serif

Colors
0255a3
f37122

```html
<!DOCTYPE html>
<html lang="en">
<head>
<meta charset="utf-8">
<title>Brindle Financial Advice – Employer Benefits Program</title>
<link href="https://fonts.googleapis.com/css2?family=Arimo:wght@400;700&family=Roboto+Condensed:wght@700&display=swap" rel="stylesheet">
<style>
  :root {
    --brand-blue: #0255a3;
    --brand-orange: #f37122;
    --bar-blue: #074a9b;
    --sky-top: #4f86cc;
    --sky-bottom: #dbe8f6;
    --ink: #222222;
    --rule: #d4d4d4;
    --paper: #ffffff;
  }
  html, body {
    margin: 0;
    padding: 0;
    overflow: hidden;
    background: var(--paper);
  }
  .page {
    position: relative;
    width: 927px;
    height: 1200px;
    overflow: hidden;
    background: var(--paper);
    font-family: "Arimo", Arial, sans-serif;
    color: var(--ink);
  }
  .side-bar {
    position: absolute;
    top: 0;
    right: 0;
    width: 104px;
    height: 1200px;
    background: var(--bar-blue);
  }
  .hero-photo {
    position: absolute;
    top: 0;
    left: 0;
    width: 823px;
    height: 588px;
    background: linear-gradient(180deg, var(--sky-top) 0%, var(--sky-bottom) 100%);
  }
  .hero-title {
    position: absolute;
    left: 57px;
    top: 446px;
    margin: 0;
    line-height: 1;
  }
  .hero-title .title-lead {
    display: block;
    font-weight: 700;
    font-size: 73px;
    letter-spacing: -1px;
    color: var(--brand-orange);
  }
  .hero-title .title-main {
    display: block;
    margin-top: 0;
    font-family: "Roboto Condensed", "Arial Narrow", sans-serif;
    font-weight: 700;
    font-size: 47px;
    color: var(--brand-blue);
  }
  .intro {
    position: absolute;
    left: 58px;
    top: 596px;
    width: 264px;
    font-size: 13.6px;
    line-height: 21.4px;
  }
  .intro p { margin: 0; }
  .intro .section-label { font-weight: 700; }
  .services {
    position: absolute;
    left: 342px;
    top: 592px;
    width: 462px;
    font-size: 13.6px;
    line-height: 21.4px;
  }
  .services .lead-in { margin: 0 0 7px 5px; }
  .service-table {
    width: 100%;
    border-collapse: collapse;
  }
  .service-table th,
  .service-table td {
    border: 1px solid var(--rule);
    vertical-align: top;
    text-align: left;
    padding: 1px 6px 2px;
  }
  .service-table th {
    width: 144px;
    font-weight: 700;
  }
  .row-choose td, .row-choose th { height: 83px; }
  .row-setup td, .row-setup th { height: 117px; }
  .row-manage td, .row-manage th { height: 127px; }
  .row-policy td, .row-policy th { height: 105px; }
  .row-update td, .row-update th { height: 62px; }
</style>
</head>
<body>
<div class="page">
  <div class="hero-photo" role="img" aria-label="Photograph of a street signpost against a blue sky, its arms reading Support, Help, Advice, Guidance and Assistance"></div>

  <h1 class="hero-title">
    <span class="title-lead">Employer</span>
    <span class="title-main">Benefits Program</span>
  </h1>

  <div class="side-bar"></div>

  <div class="intro">
    <p class="section-label">CORE:</p>
    <p>Corporate Superannuation Services<br>
    Brindle’s core offer is the ongoing support of the group employer superannuation solution.</p>
    <p>Superannuation is a long-term investment so it’s crucial to have the right partner who will consistently deliver outstanding support to you and your employees.</p>
    <p>Brindle has an extensive knowledge of superannuation providers in the market and can ensure that you have the right solution for your long-term business requirements.</p>
    <p>We are able to take over the servicing of the current group plan, or assist in setting up a plan for companies new to the market.</p>
    <p>The program we deliver has two unique components. Firstly, services to assist employers in providing a ‘best of breed’ superannuation solution to employees and secondly, proactive advice to employees to ensure that they take control of their individual financial situation.</p>
    <p>Below is an overview of the services and</p>
  </div>

  <div class="services">
    <p class="lead-in">support Brindle provides to employers:</p>
    <table class="service-table">
      <tr class="row-choose">
        <th>Choosing your employer super plan</th>
        <td>Whether you are self-directed, or seeking a full advice service, we can assist you in your selection of the most suitable provider for your employees long-term retirement needs.</td>
      </tr>
      <tr class="row-setup">
        <th>Setting up a new super plan</th>
        <td>We facilitate the complete application process, induction presentations for employees, lost super searches and the setting up of the online clearing facility for all your superannuation payments.</td>
      </tr>
      <tr class="row-manage">
        <th>Managing and Reviewing your employer super plan</th>
        <td>We work together to build and deliver your annual Client Service Plan. We manage the annual review process, provide access to all relevant information and answer all employer and employee queries, complaints and facilitate the ongoing plan administration.</td>
      </tr>
      <tr class="row-policy">
        <th>Policy Committee management</th>
        <td>We establish and manage a Policy Committee where required or desired. Responsibilities include initiating all meetings, preparing reports, minutes and the presentation of legislative product and education updates.</td>
      </tr>
      <tr class="row-update">
        <th>Keeping you up to date</th>
        <td>We provide you with all relevant communications to ensure that you meet your responsibilities and obligations.</td>
      </tr>
    </table>
  </div>
</div>
</body>
</html>
```